lab equipment website

We need a fresh new look for a company website called tarvio. We will be using the current logo and brand colors on their current website tarvio.com. They want to keep their text and on-page SEO, but would like to reformat it to look more modern and fresh. They want to have everything be high performance with a great user experience. Their main call to action is for people to fill in a contact form so they can call them. There is some information that is purposely above the fold on the instrument pages. I will need the home page, about page and a leasing page.

```html
<!DOCTYPE html>
<html lang="en">
<head>
<meta charset="utf-8">
<title>tarvio — lab equipment service and leasing</title>
<link href="https://fonts.googleapis.com/css2?family=Montserrat:wght@400;600;700&family=Roboto:wght@300;400;500;700&display=swap" rel="stylesheet">
<style>
:root{
  --teal:#17b79a;
  --teal-dark:#0f9a82;
  --ink:#2f2f2f;
  --bar:#3a3b3d;
  --nav:#3f4043;
  --mint:#e9f7f3;
  --mint-soft:#f3fbf9;
  --grey:#eeeeee;
  --line:#d9d9d9;
  --text:#555;
  --muted:#8a8a8a;
  --red:#e53935;
  --white:#fff;
}
*{margin:0;padding:0;box-sizing:border-box}
html,body{width:1200px;height:1200px;overflow:hidden;background:var(--white)}
body{font-family:"Roboto",Arial,sans-serif;color:var(--ink)}
.stage{position:absolute;left:0;top:0;width:1500px;height:1500px;transform:scale(.8);transform-origin:0 0}
.page{position:absolute;left:454px;top:0;width:592px;height:1500px;background:linear-gradient(90deg,var(--mint) 0%,var(--white) 70%);overflow:hidden}
.abs{position:absolute}
.teal{color:var(--teal)}

/* top bar */
.topbar{left:0;top:0;width:592px;height:18px;background:var(--bar);font-size:4.5px;color:#bbb}
.social{display:flex;gap:4px;position:absolute;top:5px}
.social i{display:block;width:8px;height:8px;border-radius:50%;background:#e6e6e6}
.topbar .addr{left:170px;top:6px}
.topbar .mail{left:340px;top:6px}
.topbar .phone{left:438px;top:3px;font-size:9px;color:var(--teal);font-weight:500}
.topbar .sep{top:4px;width:1px;height:10px;background:#666}

/* nav */
.nav{left:0;top:18px;width:592px;height:42px;background:var(--nav)}
.logo{display:flex;align-items:center;gap:3px;font-family:"Montserrat",sans-serif;font-weight:700;color:var(--white)}
.logo b{display:block;border-radius:50%;background:var(--teal)}
.nav .logo{left:86px;top:12px;font-size:10px}
.nav .logo b{width:7px;height:7px}
.nav .tag{left:97px;top:25px;font-size:3.5px;color:var(--teal);line-height:4px}
.navitem{top:0;width:36px;height:42px;text-align:center;font-size:3.8px;color:#aaa;padding-top:12px}
.navitem svg{display:block;margin:0 auto 6px}
.navitem.active{background:#e2e2e2;color:#777}
.cart{left:476px;top:0;width:28px;height:42px;background:var(--teal);display:flex;align-items:center;justify-content:center}

/* hero */
.hero{left:0;top:60px;width:592px;height:187px;background:linear-gradient(90deg,#e6f6f1,#f6fcfa 60%,#eef8f5)}
.search{left:251px;top:7px;font-size:5px;font-weight:700;display:flex;align-items:center;gap:4px}
.search input{width:84px;height:8px;border:0;background:var(--white);font-size:4px;padding-left:3px}
.search span.go{width:27px;height:8px;background:var(--ink);display:block}
.hero h1{left:87px;top:44px;font-size:18px;font-weight:300;color:var(--ink)}
.hero .rule{left:87px;top:66px;width:66px;height:2px;background:var(--teal)}
.hero h2{left:87px;top:74px;font-family:"Montserrat",sans-serif;font-size:15px;font-weight:700;color:var(--ink)}
.hero p{left:87px;top:102px;width:207px;font-size:6.6px;line-height:11px;color:var(--text);text-align:justify}
.btn{display:inline-block;font-size:5px;font-weight:700;color:var(--white);text-align:center;line-height:17px;height:17px}
.hero .btn1{left:87px;top:152px;width:62px;background:var(--teal)}
.hero .btn2{left:149px;top:152px;width:62px;background:var(--ink)}
.hero .visual{left:305px;top:35px;width:200px;height:125px;border-radius:6px;background:radial-gradient(ellipse at 45% 60%,#d8dde3,#f0f3f5 70%,rgba(255,255,255,0))}
.arrow{width:18px;height:18px;border-radius:50%;background:rgba(0,0,0,.06)}
.dots{display:flex;gap:6px}
.dots i{display:block;width:4px;height:4px;border-radius:50%;border:1px solid var(--teal)}
.dots i.on{background:var(--teal)}

/* products */
.products{left:0;top:247px;width:592px;height:142px;background:var(--grey)}
.card{top:12px;width:98px;height:98px;background:var(--white);border:2px solid #ddd}
.card.active{border-color:var(--teal)}
.card .shot{position:absolute;left:6px;top:6px;right:6px;bottom:24px;background:linear-gradient(#f2f2f2,#dcdcdc)}
.card .label{position:absolute;left:0;right:0;top:64px;height:16px;background:rgba(255,255,255,.75);text-align:center;font-size:7px;font-weight:500;line-height:16px;color:var(--ink)}
.card.active .label{color:var(--teal)}
.card .pin{position:absolute;left:43px;bottom:-7px;width:11px;height:11px;background:var(--ink);transform:rotate(45deg)}
.card.active .pin{background:var(--teal)}

/* hours */
.hours-bar{left:87px;top:405px;width:415px;height:19px;background:var(--teal);color:var(--white);font-family:"Montserrat",sans-serif;font-size:8px;letter-spacing:5px;text-align:center;line-height:19px;padding-right:40px}
.hours-hex{left:407px;top:394px}
.hours-table{left:102px;top:436px;width:386px;font-size:5.5px;color:var(--ink);font-weight:500}
.hrow{position:absolute;width:180px;height:18px;border-bottom:1px solid var(--line);display:flex;align-items:center}
.hrow .d{width:94px}
.hrow .t{color:var(--teal)}
.hrow .t.closed{color:var(--red)}

/* text sections */
.eyebrow{font-family:"Montserrat",sans-serif;font-size:6.6px;letter-spacing:1.6px;font-weight:600;color:var(--ink);line-height:8px}
.eyebrow em{font-style:normal;color:var(--teal)}
.copy{font-size:4.6px;line-height:11px;color:var(--muted)}
.copy b{color:var(--ink)}
.btn-sm{height:7px;width:36px;background:var(--teal);border-radius:1px}

/* skills */
.skill-ico{width:24px;height:24px;border-radius:50%;background:var(--teal);display:flex;align-items:center;justify-content:center}
.skill-txt{font-size:5px;color:var(--text);text-align:center;width:120px}
.skill-view{font-size:4px;color:var(--teal);font-weight:700}
.meter{width:172px}
.meter .lbl{font-size:4px;font-weight:700;color:var(--ink);margin-bottom:2px}
.meter .track{height:4px;background:#e0e0e0;border-radius:2px;overflow:hidden}
.meter .fill{height:4px;background:var(--teal);border-radius:2px}

/* management */
.mgmt{left:87px;top:1152px;width:415px;height:127px;background:linear-gradient(180deg,#6b6e72,#3d4043 55%,#7b7e82)}
.mgmt h3{position:absolute;left:33px;top:10px;font-family:"Montserrat",sans-serif;font-size:22px;letter-spacing:5px;color:rgba(255,255,255,.85);font-weight:700}
.mgmt .mlogo{left:340px;top:36px;font-size:8px}
.mgmt .mlogo b{width:6px;height:6px}
.person{width:92px;height:124px;background:var(--white);box-shadow:0 2px 6px rgba(0,0,0,.15);text-align:center;padding:14px 8px 0}
.person .nm{font-size:4px;font-weight:700;color:var(--teal)}
.person .rl{font-size:3.4px;color:var(--ink);margin:3px 0 6px}
.person p{font-size:3.9px;line-height:7.4px;color:var(--text);text-align:justify}
.avatar{width:26px;height:26px;border-radius:50%;border:2px solid var(--white);background:linear-gradient(#c9b9a8,#8d7a68)}

/* footer */
.footer{left:0;top:1372px;width:592px;height:91px;background:var(--bar);color:#ccc}
.footer .flogo{left:86px;top:9px;font-size:8px}
.footer .flogo b{width:6px;height:6px}
.footer .about{left:87px;top:28px;width:90px;font-size:3.8px;line-height:9.2px;color:#bbb;text-align:justify}
.fhead{font-size:5px;font-weight:700;color:var(--white);padding-bottom:4px;border-bottom:1px solid var(--red)}
.flinks{font-size:4.2px;line-height:11px;color:#ddd;font-weight:500}
.finput{width:98px;height:9px;background:#d6d6d6;font-size:3px;color:#888;padding:3px 0 0 4px}
.fsub{width:98px;height:9px;background:var(--teal);font-size:4px;color:var(--white);letter-spacing:3px;text-align:center;line-height:9px;font-weight:700}
.fsocial{display:flex;gap:8px}
.fsocial i{display:block;width:10px;height:10px;border-radius:50%;background:#eee}
.strip{left:0;top:1463px;width:592px;height:17px;background:#606265;font-size:4px;color:#ddd;text-align:center;line-height:17px}
.copyright{left:0;top:1480px;width:592px;height:20px;background:#2c2d2f;font-size:4px;color:#ddd;text-align:center;line-height:20px;font-weight:500}
</style>
</head>
<body>
<div class="stage">
<div class="page">

  <!-- top bar -->
  <div class="abs topbar">
    <div class="social" style="left:88px"><i></i><i></i><i></i><i></i></div>
    <div class="abs sep" style="left:155px"></div>
    <svg class="abs" style="left:169px;top:5px" width="5" height="7" viewBox="0 0 10 14"><path d="M5 0a5 5 0 0 0-5 5c0 4 5 9 5 9s5-5 5-9a5 5 0 0 0-5-5z" fill="#999"/></svg>
    <div class="abs addr" style="left:180px">48 Alder Row Suite 310 Fairhaven, CA 90210</div>
    <div class="abs sep" style="left:324px"></div>
    <svg class="abs" style="left:338px;top:6px" width="8" height="5" viewBox="0 0 16 10"><rect x="0.5" y="0.5" width="15" height="9" fill="none" stroke="#999"/><path d="M1 1l7 5 7-5" fill="none" stroke="#999"/></svg>
    <div class="abs mail" style="left:352px">hello@tarvio.com</div>
    <div class="abs sep" style="left:424px"></div>
    <div class="abs phone">(555) 014-2290</div>
  </div>

  <!-- nav -->
  <div class="abs nav">
    <div class="abs logo"><b></b>tarvio</div>
    <div class="abs tag">good services,<br>lab support.</div>
    <div class="abs navitem active" style="left:170px">
      <svg width="9" height="8" viewBox="0 0 18 16"><path d="M9 0L0 8h3v8h4v-5h4v5h4V8h3z" fill="var(--teal)"/></svg>HOME</div>
    <div class="abs navitem" style="left:207px">
      <svg width="8" height="8" viewBox="0 0 16 16"><circle cx="8" cy="8" r="7" fill="#888"/></svg>ABOUT</div>
    <div class="abs navitem" style="left:246px">
      <svg width="8" height="8" viewBox="0 0 16 16"><rect x="1" y="1" width="14" height="14" fill="none" stroke="#888" stroke-width="2"/><path d="M4 8l3 3 5-6" fill="none" stroke="#888" stroke-width="2"/></svg>LEASING</div>
    <div class="abs navitem" style="left:283px">
      <svg width="8" height="8" viewBox="0 0 16 16"><circle cx="8" cy="8" r="6.5" fill="none" stroke="#888" stroke-width="2"/><path d="M8 4v4l3 2" fill="none" stroke="#888" stroke-width="2"/></svg>FAQ</div>
    <div class="abs navitem" style="left:322px;width:48px">
      <svg width="6" height="8" viewBox="0 0 10 14"><path d="M5 0a5 5 0 0 0-5 5c0 4 5 9 5 9s5-5 5-9a5 5 0 0 0-5-5z" fill="#888"/></svg>CONTACT INFO</div>
    <div class="abs cart"><svg width="12" height="11" viewBox="0 0 24 22"><path d="M1 2h4l3 12h12l3-9H7" fill="none" stroke="#fff" stroke-width="2.4"/><circle cx="10" cy="19" r="2" fill="#fff"/><circle cx="18" cy="19" r="2" fill="#fff"/></svg></div>
  </div>

  <!-- hero -->
  <div class="abs hero">
    <div class="abs search"><span><span class="teal">HELP YOU TO FIND</span> WHAT YOU ARE LOOKING !</span><input value="Search keyword here" aria-label="Search"><span class="go"></span></div>
    <div class="abs arrow" style="left:24px;top:103px"></div>
    <div class="abs arrow" style="left:540px;top:103px"></div>
    <h1 class="abs">Our goal is simple:</h1>
    <div class="abs rule"></div>
    <h2 class="abs"><span class="teal">Save labs</span> Time <span class="teal">&amp;</span> Money</h2>
    <p class="abs"><b>tarvio</b> is a lab support program that provides scientists with comprehensive maintenance/repair coverage and operating lease solutions at an affordable price.</p>
    <div class="abs btn btn1">LEARN MORE</div>
    <div class="abs btn btn2">REQUEST LEASE</div>
    <div class="abs visual" role="img" aria-label="Group of laboratory instruments: analyser, chromatography stack and microscope"></div>
    <div class="abs dots" style="left:467px;top:160px"><i class="on"></i><i></i><i></i><i></i></div>
  </div>

  <!-- products -->
  <div class="abs products">
    <div class="abs card active" style="left:87px"><div class="shot" role="img" aria-label="Autoclave photo"></div><div class="label">AUTOCLAVE</div><div class="pin"></div></div>
    <div class="abs card" style="left:193px"><div class="shot" role="img" aria-label="Lab balance photo"></div><div class="label">LAB BALANCE</div><div class="pin"></div></div>
    <div class="abs card" style="left:299px"><div class="shot" role="img" aria-label="Centrifuge photo"></div><div class="label">CENTRIFUGE</div><div class="pin"></div></div>
    <div class="abs card" style="left:405px"><div class="shot" role="img" aria-label="Cryostat photo"></div><div class="label">CRYOSTAT</div><div class="pin"></div></div>
    <div class="abs dots" style="left:279px;top:125px"><i class="on"></i><i></i><i></i><i></i></div>
  </div>

  <!-- operating hours -->
  <div class="abs hours-bar">OPERATING HOURS</div>
  <svg class="abs hours-hex" width="42" height="40" viewBox="0 0 42 40"><polygon points="11,1 31,1 41,20 31,39 11,39 1,20" fill="#fff" stroke="var(--teal)" stroke-width="2"/><circle cx="21" cy="20" r="7" fill="none" stroke="var(--teal)" stroke-width="1.6"/><path d="M21 16v4h3" fill="none" stroke="var(--teal)" stroke-width="1.4"/></svg>
  <div class="abs hours-table">
    <div class="hrow" style="left:0;top:0"><span class="d">Monday</span><span class="t">7:00 AM - 6:00 PM</span></div>
    <div class="hrow" style="left:0;top:18px"><span class="d">Tuesday</span><span class="t">7:00 AM - 6:00 PM</span></div>
    <div class="hrow" style="left:0;top:35px;border:0"><span class="d">Wednesday</span><span class="t">7:00 AM - 6:00 PM</span></div>
    <div class="hrow" style="left:209px;top:0"><span class="d">Thursday</span><span class="t">7:00 AM - 6:00 PM</span></div>
    <div class="hrow" style="left:209px;top:18px"><span class="d">Friday</span><span class="t">7:00 AM - 6:00 PM</span></div>
    <div class="hrow" style="left:209px;top:35px;border:0"><span class="d">Saturday | Sunday</span><span class="t closed">Closed</span></div>
  </div>

  <!-- trusted -->
  <div class="abs eyebrow" style="left:118px;top:506px;width:360px"><em>TRUSTED COMPANY OFFERING</em> SCIENTIFIC EQUIPMENT SERVICE PLANS AND FLEXIBLE LEASES</div>
  <p class="abs copy" style="left:118px;top:536px;width:352px">&nbsp;&nbsp;&nbsp;&nbsp;&nbsp;&nbsp;At <b>tarvio</b>, our goal is to ensure the success of your business. Whether you are running a laboratory or other scientific facilities, we want to keep you provided with the best in cutting-edge equipment. That's why we offer flexible scientific equipment leasing options with worry-free service plans- to provide your business with the tools needed to perform at its peak.</p>
  <div class="abs btn-sm" style="left:279px;top:589px"></div>

  <!-- needs -->
  <div class="abs eyebrow" style="left:118px;top:625px"><em>WE UNDERSTAND YOUR NEEDS</em> BECAUSE WE ARE SCIENTIST FIRST</div>
  <p class="abs copy" style="left:118px;top:647px;width:352px">&nbsp;&nbsp;&nbsp;&nbsp;&nbsp;&nbsp;At <b>tarvio</b>, our goal is to ensure the success of your business. Whether you are running a laboratory or other scientific facilities, we want to keep you provided with the best in cutting-edge equipment. That's why we offer flexible scientific equipment leasing options with worry-free service plans- to provide your business with the tools needed to perform at its peak.</p>
  <svg class="abs" style="left:261px;top:693px" width="68" height="68" viewBox="0 0 68 68">
    <circle cx="34" cy="34" r="31" fill="none" stroke="#e2e2e2" stroke-width="3"/>
    <path d="M34 3a31 31 0 1 1-29 42" fill="none" stroke="var(--teal)" stroke-width="3"/>
    <circle cx="34" cy="34" r="24" fill="none" stroke="#a6dccd" stroke-width="4"/>
    <circle cx="34" cy="34" r="18" fill="#2d4a5c"/>
    <text x="34" y="33" font-size="2.6" fill="#fff" text-anchor="middle" font-family="Roboto">We have you</text>
    <text x="34" y="37" font-size="2.6" fill="#fff" text-anchor="middle" font-family="Roboto">covered</text>
  </svg>
  <p class="abs" style="left:118px;top:782px;width:166px;font-size:4.8px;line-height:11px;font-weight:700;color:var(--text)">When it comes to creating innovative solutions that cater to your lab, tarvio's dedicated team of problem-solvers has got you covered. Here's how we save you time and money:</p>
  <div class="abs btn-sm" style="left:246px;top:824px"></div>
  <div class="abs" style="left:298px;top:782px;width:1px;height:60px;background:var(--line)"></div>
  <p class="abs copy" style="left:310px;top:782px;width:160px;line-height:9.2px">We regularly provide businesses with what they need to improve their budget and efficiency. We offer laboratory equipment leasing for a wide range of needs. If you want to discuss your needs more in-depth.</p>
  <p class="abs copy" style="left:310px;top:822px;width:170px">Don't hesitate to call us at <span class="teal" style="font-size:8px;font-weight:500">(555) 014-2290</span> or fill out our<br><span class="teal" style="font-size:5px;text-decoration:underline">Contact form</span></p>

  <!-- skills -->
  <div class="abs eyebrow" style="left:118px;top:872px"><em>OUR</em> SKILLS</div>
  <div class="abs" style="left:118px;top:884px;width:370px;height:1px;background:var(--line)"></div>

  <div class="abs skill-ico" style="left:163px;top:902px"><svg width="12" height="12" viewBox="0 0 24 24"><path d="M9 2h6M10 2v7L4 20h16L14 9V2" fill="none" stroke="#fff" stroke-width="2.2"/></svg></div>
  <div class="abs skill-txt" style="left:115px;top:939px">Knowledge of the laboratory</div>
  <div class="abs" style="left:115px;top:948px;width:120px;height:1px;background:var(--line)"></div>
  <div class="abs skill-view" style="left:166px;top:953px">View →</div>

  <div class="abs skill-ico" style="left:163px;top:980px"><svg width="12" height="12" viewBox="0 0 24 24"><rect x="3" y="7" width="18" height="13" fill="#fff"/><path d="M9 7V4h6v3" fill="none" stroke="#fff" stroke-width="2"/><path d="M12 10v7M8.5 13.5h7" stroke="var(--teal)" stroke-width="2"/></svg></div>
  <div class="abs skill-txt" style="left:115px;top:1017px">Worry free lab equipment PM/repair coverage.</div>
  <div class="abs" style="left:115px;top:1026px;width:120px;height:1px;background:var(--line)"></div>
  <div class="abs skill-view" style="left:166px;top:1031px">View →</div>

  <div class="abs skill-ico" style="left:163px;top:1058px"><svg width="12" height="12" viewBox="0 0 24 24"><path d="M4 4l6 6-3 3 6 6 7-7-6-6-3 3" fill="none" stroke="#fff" stroke-width="2.2"/></svg></div>
  <div class="abs skill-txt" style="left:115px;top:1095px">Cost-effective lease structures and payment plans.</div>
  <div class="abs skill-view" style="left:166px;top:1115px">View →</div>

  <div class="abs" style="left:290px;top:900px;width:100px;height:100px;background:linear-gradient(135deg,rgba(23,183,154,.15),rgba(245,160,40,.35));border-radius:4px" role="img" aria-label="Illustration of a person climbing step blocks toward a target"></div>

  <div class="abs meter" style="left:291px;top:1018px"><div class="lbl">Cost Saving</div><div class="track"><div class="fill" style="width:97%"></div></div></div>
  <div class="abs meter" style="left:291px;top:1034px"><div class="lbl">Lease Plan Flexibility</div><div class="track"><div class="fill" style="width:95%"></div></div></div>
  <div class="abs meter" style="left:291px;top:1049px"><div class="lbl">Customer Service</div><div class="track"><div class="fill" style="width:100%"></div></div></div>
  <div class="abs" style="left:291px;top:1076px;font-size:6px;font-weight:500;color:var(--ink)">The Competition</div>
  <div class="abs meter" style="left:291px;top:1092px"><div class="lbl">Reliability</div><div class="track"><div class="fill" style="width:27%"></div></div></div>
  <div class="abs meter" style="left:291px;top:1107px"><div class="lbl">Continued Support</div><div class="track"><div class="fill" style="width:10%"></div></div></div>

  <!-- management -->
  <div class="abs mgmt" role="img" aria-label="Black and white city skyline photo">
    <h3>THE TOP MANAGEMENT</h3>
    <div class="abs logo mlogo"><b></b>tarvio</div>
  </div>
  <div class="abs person" style="left:122px;top:1212px"><div class="nm">LEO MARSH</div><div class="rl">Lab Relations</div><p>" My time spent in the lab opened my eyes to the passion and dedication that drives scientists, as well as the frustration of a tight budget and equipment upkeep. tarvio was created in order to help overcome these obstacles and enable scientists to focus on what they're truly passionate about: research. "</p></div>
  <div class="abs person" style="left:252px;top:1212px"><div class="nm">DANA HOLT</div><div class="rl">Finance</div><p>" tarvio's success is measured by our customers' financial savings and productivity, making your laboratory's interests our main priority. The more time and money we save you, the better we've done our job. "</p></div>
  <div class="abs person" style="left:382px;top:1212px"><div class="nm">RAVI SEN</div><div class="rl">Operations</div><p>" The core of my involvement in tarvio extends far beyond business development. My goal is to see that researchers and scientists are provided with an effective operational solution, so that together we can be a driving force in the progress of science. "</p></div>
  <div class="abs avatar" style="left:109px;top:1198px" role="img" aria-label="Portrait of Leo Marsh"></div>
  <div class="abs avatar" style="left:241px;top:1196px" role="img" aria-label="Portrait of Dana Holt"></div>
  <div class="abs avatar" style="left:373px;top:1196px" role="img" aria-label="Portrait of Ravi Sen"></div>

  <!-- footer -->
  <div class="abs footer">
    <div class="abs logo flogo"><b></b>tarvio</div>
    <p class="abs about">We are a team of Westbay University scientists driven by our passion for research. We strive to serve the scientific community. We love what we do, and who we work with. Together we can make positive changes in the world of research.</p>
    <div class="abs" style="left:200px;top:9px;width:66px"><div class="fhead">QUICK LINKS</div><div class="flinks" style="margin-top:4px">Home<br>About Us<br>Leasing<br>FAQ<br>Contact Info</div></div>
    <div class="abs" style="left:292px;top:9px;width:84px"><div class="fhead">CONTACT INFO</div>
      <div style="font-size:4.6px;line-height:7px;color:#fff;font-weight:700;margin:8px 0 0 7px">48 Alder Row<br>Suite 310<br>Fairhaven, CA 90210</div>
      <div style="font-size:9px;color:var(--teal);margin:3px 0 0 7px">(555) 014-2290</div>
      <div style="font-size:4.4px;line-height:9px;color:#ddd;margin-left:7px">info@tarvio.com<br>https://tarvio.com</div>
    </div>
    <div class="abs" style="left:404px;top:9px;width:104px"><div style="font-size:5px;font-weight:700;color:#fff">ALWAYS RECEIVE NEWS LETTER ?</div>
      <div class="finput" style="margin-top:10px">Type your name</div>
      <div class="finput" style="margin-top:3px">Type your email</div>
      <div class="fsub" style="margin-top:3px">SUBSCRIBE</div>
      <div class="fsocial" style="margin-top:6px"><i></i><i></i><i></i><i></i></div>
    </div>
  </div>
  <div class="abs strip">We are a team of Westbay University scientists driven by our passion for research. We strive to serve the scientific community. We love what we do, and who we work with. Together we can make positive changes in the world of research.</div>
  <div class="abs copyright">Copyright © 2018 Tarvio Labs. All Rights Reserved.</div>

</div>
</div>
</body>
</html>
```